Food Safety 1-California workers only

3.25" by 4.5" Black and White Magazine Ad
This ad is to train California workers only.
Workers will be trained on: Food Safety, FSMA (Food Safety Modernization Act), using equipment safety, food processing production skills, worker safety, supervisory skills, communication skills.
"FREE TRAINING", The company does the training or Keystone Learning will provide the training.
Training grants range from $100,000 to $400,000.
Companies must be in business for profit.
Companies must train 200 employees or more.
This program is for California workers only.
Incumbent or new-hires are eligible.

Target Market(s)

California food processors, farms, food packaging, food processors, companies under FSMA, food safety, food production who need to train employees.

Industry/Entity Type

Food Production

Font styles to use
Serif
Sans Serif

Colors

Designer to choose colors to be used in the design.

Requirements
Must have
• This is a 3.25 inch by 4.5 inch magazine ad. It must be black and white. No color.
• The deliverable must be in basic PhotoShop. The ad does not need to include any graphics and be text only if needed. If you have a black and white graphic that will show well.
• Look at www.KLGFoodSafety..com
• Use the text from "MEALBOX-Photoshop-052018" file as your starting point.
Nice to have
• A black and white graphic about food. See www.KLGFoodSafety.com
Should not have
• No color.

```html
<!DOCTYPE html>
<html lang="en">
<head>
<meta charset="utf-8">
<title>Free Training – Keystone Learning</title>
<link rel="stylesheet" href="https://fonts.googleapis.com/css2?family=Montserrat:wght@900&family=Oswald:wght@400&family=Roboto+Condensed:wght@400&family=Source+Sans+3:wght@600;800&display=swap">
<style>
  :root {
    --ink: #1f1e20;
    --paper: #ffffff;
    --paper-soft: #f1f1f1;
  }
  * { margin: 0; padding: 0; box-sizing: border-box; }
  html, body { width: 867px; height: 1200px; overflow: hidden; background: var(--paper); }
  .ad { position: relative; width: 867px; height: 1200px; overflow: hidden; background: var(--paper); color: var(--ink); }

  .food-artwork {
    position: absolute; left: 155px; top: 0; width: 712px; height: 1200px;
    background: radial-gradient(ellipse at 55% 50%, var(--paper) 35%, var(--paper-soft) 100%);
  }

  .side-band { position: absolute; left: 0; top: 0; width: 155px; height: 1200px; background: var(--ink); }
  .side-band svg { position: absolute; left: 0; top: 0; }
  .headline { font-family: "Montserrat", sans-serif; font-weight: 900; font-size: 112px; fill: var(--paper); }

  .topics {
    position: absolute; left: 300px; top: 288px; list-style: none;
    font-family: "Oswald", sans-serif; font-size: 38px; line-height: 44.5px; color: var(--ink);
  }
  .topics li::before { content: "•"; display: inline-block; width: 33px; font-size: 28px; vertical-align: 4px; }

  .promise { position: absolute; right: 0; top: 452px; font-family: "Oswald", sans-serif; font-size: 39px; line-height: 44px; text-align: right; }
  .promise span { display: block; margin-left: auto; background: var(--ink); color: var(--paper); padding-right: 42px; }
  .promise .l1 { width: 235px; height: 60px; padding-top: 12px; }
  .promise .l2 { width: 212px; height: 40px; }
  .promise .l3 { width: 235px; height: 40px; }
  .promise .l4 { width: 263px; height: 56px; }

  .qualify { position: absolute; left: 191px; top: 603px; }
  .qualify h2 { font-family: "Source Sans 3", sans-serif; font-weight: 800; font-size: 23px; line-height: 30px; }
  .qualify ul { list-style: none; font-family: "Roboto Condensed", sans-serif; font-size: 24px; line-height: 31.5px; }
  .qualify li::before { content: "•"; display: inline-block; width: 29px; }

  .contact-block { position: absolute; right: 0; top: 927px; font-family: "Source Sans 3", sans-serif; font-size: 25px; text-align: right; }
  .contact-block span { display: block; margin-left: auto; background: var(--ink); color: var(--paper); padding-right: 44px; height: 33px; line-height: 33px; }
  .contact-block .label { font-weight: 800; width: 175px; height: 40px; line-height: 44px; }
  .contact-block .person { width: 222px; }
  .contact-block .company { width: 409px; }
  .contact-block .street { width: 453px; }
  .contact-block .city { width: 258px; height: 36px; }

  .web-lines { position: absolute; left: 0; top: 1008px; font-family: "Source Sans 3", sans-serif; font-weight: 600; font-size: 25px; color: var(--paper); }
  .web-lines span { display: block; height: 34px; line-height: 34px; padding-left: 42px; background: var(--ink); }
  .web-lines .w1 { width: 262px; }
  .web-lines .w2 { width: 340px; }
  .web-lines .w3 { width: 393px; }
  .web-lines .w4 { width: 324px; }
</style>
</head>
<body>
<div class="ad">
  <div class="food-artwork" role="img" aria-label="Black line illustration of a table seen from above with plates, cups, teapot, fruit, bread and hands reaching for food"></div>

  <div class="side-band">
    <svg width="155" height="1200" viewBox="0 0 155 1200" aria-label="Free Training">
      <text class="headline" transform="translate(121 976) rotate(-90)" textLength="826" lengthAdjust="spacingAndGlyphs">FREE TRAINING</text>
    </svg>
  </div>

  <ul class="topics">
    <li>FOOD SAFETY</li>
    <li>FSMA</li>
    <li>PRODUCTION SKILLS</li>
    <li>WORKER SAFETY</li>
  </ul>

  <div class="promise">
    <span class="l1">We Do The</span>
    <span class="l2">TRAINING</span>
    <span class="l3">&amp; The State</span>
    <span class="l4">PAYS FOR YOU</span>
  </div>

  <section class="qualify">
    <h2>How to qualify:</h2>
    <ul>
      <li>Train California Workers Only</li>
      <li>Trainees must earn $11/hour</li>
      <li>Full-time workers only</li>
      <li>Employees must attend at least 8 Hours of training</li>
      <li>You must train 200 or more employees</li>
      <li>Incumbent or New-Hire workers are eligible</li>
      <li>Seasonal workers are eligible</li>
    </ul>
  </section>

  <address class="contact-block" style="font-style:normal">
    <span class="label">Contact:</span>
    <span class="person">Daniel Marsh</span>
    <span class="company">Keystone Learning Company, Inc.</span>
    <span class="street">2100 Harbor Crest Drive, Suite 310</span>
    <span class="city">Irvine, CA 92618</span>
  </address>

  <div class="web-lines">
    <span class="w1">www.KLGCAL.com</span>
    <span class="w2">www.KLGFoodSafety.com</span>
    <span class="w3">Email: Dan.Marsh@KLGCAL.com</span>
    <span class="w4">Phone: (949) 555-0142</span>
  </div>
</div>
</body>
</html>
```